New Business Card Design for Engineering and Surveying Company

We need a new design template for our business cards. We are a civil engineering, land surveying and pipeline integrity business. Please see dkhpartners.com for details. We need a bold, new business card design to complement our rebranding and marketing program. We have anew logo and attached vectro file. Please find additional details below. I am available to answer any questions.

Target Market(s)

Contractors, business owners, oil companies

Contact Information for Business Card

Needs to be customizable for different people (name, title, cell)

Font styles to use
Sans Serif
Other font styles liked:
• See eps file

Requirements
Must have
• Example Information:
Trevor Ashcombe

T:409-555-0173
M: 202-555-0148
tashcombe@dkhprtnrs.com

Address: 1875 Pinecrest Parkway, Beaumont, Texas 77703
Email: tolvanrey@dkhpartners.com
Website: www.dkhpartners.com
Nice to have
• I would like the back of the card to have the logo on a bold background with the text below:

[logo]
DORAN KESSLING & PARTNERS
CIVIL ENGINEERING | LAND SURVEYING | PIPELINE INTEGRITY

The reverse side should have the contact information for the person (example above), a smaller version of the logo and a graphic

```html
<!DOCTYPE html>
<html lang="en">
<head>
<meta charset="utf-8">
<title>DKH Partners – Business Card</title>
<link rel="stylesheet" href="https://fonts.googleapis.com/css2?family=Montserrat:wght@500;700;800&family=Work+Sans:wght@400;500;700&display=swap">
<style>
  :root {
    --stage: #2b2b2d;
    --card-white: #ffffff;
    --card-black: #1c1c1d;
    --brand-blue: #1f4fa8;
    --brand-red: #e41d2d;
    --ink: #161616;
    --text-grey: #4a4a4a;
    --white: #ffffff;
  }
  * { box-sizing: border-box; margin: 0; padding: 0; }
  html, body { width: 1200px; height: 900px; overflow: hidden; }
  body {
    background: var(--stage);
    display: flex;
    flex-direction: column;
    align-items: center;
    justify-content: center;
    gap: 50px;
    font-family: "Work Sans", Arial, sans-serif;
  }
  .card {
    position: relative;
    width: 680px;
    height: 390px;
    border-radius: 4px;
    overflow: hidden;
    box-shadow: 0 10px 30px rgba(0,0,0,.45);
  }

  /* Front */
  .card-front { background: var(--card-white); }
  .card-front .wordmark {
    position: absolute;
    left: 44px;
    top: 92px;
    display: flex;
    align-items: center;
    gap: 14px;
  }
  .wordmark-square {
    width: 26px; height: 26px;
    background: var(--brand-red);
  }
  .wordmark-name {
    font-family: "Montserrat", Arial, sans-serif;
    font-weight: 800;
    font-size: 86px;
    letter-spacing: 2px;
    line-height: 1;
  }
  .card-front .wordmark-name { color: var(--ink); }
  .divider {
    position: absolute;
    left: 318px;
    top: 52px;
    width: 2px;
    height: 196px;
    background: var(--brand-blue);
  }
  .contact {
    position: absolute;
    left: 344px;
    top: 52px;
    color: var(--text-grey);
    font-size: 16px;
    line-height: 1.35;
  }
  .contact-name {
    font-family: "Montserrat", Arial, sans-serif;
    font-weight: 800;
    font-size: 25px;
    color: var(--brand-blue);
    line-height: 1.1;
  }
  .contact-title { font-size: 17px; margin-bottom: 6px; }
  .contact-address { margin-bottom: 6px; }
  .contact-row { display: flex; align-items: center; gap: 8px; }
  .contact-row svg { width: 13px; height: 13px; flex: none; }
  .wave { position: absolute; left: 0; top: 0; }
  .website {
    position: absolute;
    left: 40px;
    bottom: 16px;
    color: var(--white);
    font-size: 17px;
    letter-spacing: .5px;
  }

  /* Back */
  .card-back {
    background: var(--card-black);
    display: flex;
    flex-direction: column;
    align-items: center;
    justify-content: center;
  }
  .card-back .wordmark { display: flex; align-items: center; gap: 16px; margin-bottom: 26px; }
  .card-back .wordmark-name { color: var(--white); font-size: 104px; }
  .company-name {
    font-family: "Montserrat", Arial, sans-serif;
    font-weight: 700;
    font-size: 19px;
    letter-spacing: 1.5px;
    color: var(--brand-red);
    margin-bottom: 10px;
  }
  .services {
    font-family: "Montserrat", Arial, sans-serif;
    font-weight: 500;
    font-size: 15px;
    letter-spacing: 1.5px;
    color: var(--white);
  }
</style>
</head>
<body>

<section class="card card-front" aria-label="Business card front">
  <svg class="wave" width="680" height="390" viewBox="0 0 680 390" aria-hidden="true">
    <path d="M0 232 C70 290 170 318 300 326 C450 336 590 352 640 390 L0 390 Z" fill="var(--brand-blue)"/>
    <path d="M150 272 C260 312 420 318 540 330 C600 336 640 356 660 390 L640 390 C600 352 450 336 300 326 C240 322 190 300 150 272 Z" fill="var(--card-white)"/>
    <path d="M150 272 C250 306 420 308 545 320 C610 326 650 350 672 390 L660 390 C640 356 600 336 540 330 C420 318 260 312 150 272 Z" fill="var(--brand-red)"/>
  </svg>

  <div class="wordmark">
    <span class="wordmark-square"></span>
    <span class="wordmark-name">DKH</span>
  </div>

  <div class="divider"></div>

  <div class="contact">
    <p class="contact-name">Trevor Ashcombe</p>
    <p class="contact-title">President</p>
    <p class="contact-address">1875 Pinecrest Parkway<br>Beaumont, Texas 77703</p>
    <p class="contact-row">
      <svg viewBox="0 0 16 16"><path d="M3 1l3 3-1.5 2a9 9 0 0 0 5.5 5.5L12 10l3 3-2 2C7 15 1 9 1 3z" fill="var(--brand-red)"/></svg>
      409-555-0173
    </p>
    <p class="contact-row">
      <svg viewBox="0 0 16 16"><rect x="4" y="1" width="8" height="14" rx="1.5" fill="none" stroke="var(--brand-red)" stroke-width="1.8"/></svg>
      202-555-0148
    </p>
    <p class="contact-row">
      <svg viewBox="0 0 16 16"><rect x="1" y="3" width="14" height="10" fill="var(--brand-red)"/><path d="M1 3l7 6 7-6" fill="none" stroke="#fff" stroke-width="1.4"/></svg>
      tashcombe@dkhprtnrs.com
    </p>
  </div>

  <p class="website">www.dkhpartners.com</p>
</section>

<section class="card card-back" aria-label="Business card back">
  <div class="wordmark">
    <span class="wordmark-square"></span>
    <span class="wordmark-name">DKH</span>
  </div>
  <p class="company-name">DORAN KESSLING &amp; PARTNERS</p>
  <p class="services">CIVIL ENGINEERING | LAND SURVEYING | PIPELINE INTEGRITY</p>
</section>

</body>
</html>
```